Create a flyer for our party getaway to Ibiza.

'The Crimson Ibiza Escape'

Friday 14th July - Monday 17th July

DJ Morvek & DJ Tundral brings together a jam-packed weekend schedule full of the best urban parties in Ibiza.

What's included?

4 Nights Of Entertainment
6 Parties In Total
1 Boat Party
1 Pool Party
2 Superclub Parties
1 Indoor Water Party
Bottomless Drinks (Boat Party Only)
An unbelievable experience
1 unbeatable price.

All this for 140€ (you save 50€ when you book with us)

Tickets avaialble from Ticketlane & Gribolo

Target Market(s)

holiday goers

Industry/Entity Type

party, events, club, hip hop

Requirements
Must have
• good vibes
Nice to have
• nice catchy looking title

```html
<!DOCTYPE html>
<html lang="en">
<head>
<meta charset="utf-8">
<title>The Crimson Ibiza Escape</title>
<link rel="stylesheet" href="https://fonts.googleapis.com/css2?family=Saira+Condensed:wght@800&family=Syncopate:wght@700&family=Signika:wght@600&family=Montserrat:wght@300;600;700;800&family=Mr+Dafoe&display=swap">
<style>
  :root {
    --page-top: #1a0a30;
    --page-bottom: #3c1152;
    --stage-top: #2b3190;
    --stage-mid: #3b2a8c;
    --stage-bottom: #4a1c78;
    --box: rgba(14, 12, 56, 0.88);
    --gold: #ffc61a;
    --white: #ffffff;
    --orange: #f46a12;
    --date-stroke: #1c1646;
  }
  * { margin: 0; padding: 0; box-sizing: border-box; }
  html, body { width: 848px; height: 1200px; overflow: hidden; }
  body {
    position: relative;
    background: linear-gradient(180deg, var(--page-top), var(--page-bottom));
    font-family: "Montserrat", sans-serif;
    color: var(--white);
  }
  .flyer {
    position: absolute; left: 39px; top: 55px; width: 770px; height: 1088px;
    overflow: hidden;
    box-shadow: 0 6px 18px rgba(0,0,0,0.5);
  }
  .stage-photo {
    position: absolute; inset: 0;
    background:
      radial-gradient(ellipse 260px 280px at 48% 42%, rgba(220,200,240,0.35), transparent 70%),
      radial-gradient(ellipse 500px 300px at 50% 10%, rgba(200,60,160,0.35), transparent 70%),
      linear-gradient(180deg, var(--stage-top), var(--stage-mid) 55%, var(--stage-bottom));
  }
  .title { position: absolute; left: 0; top: 60px; width: 770px; height: 170px; }
  .title-main { font-family: "Saira Condensed", sans-serif; font-weight: 800; }
  .title-accent { font-family: "Syncopate", sans-serif; font-weight: 700; }
  .dates {
    position: absolute; left: 0; top: 490px; width: 770px; text-align: center;
    font-family: "Signika", sans-serif; font-weight: 600; font-size: 45px;
    letter-spacing: -0.5px; white-space: nowrap;
    -webkit-text-stroke: 7px var(--date-stroke); paint-order: stroke fill;
    text-shadow: 0 3px 6px rgba(0,0,0,0.5);
  }
  .dates sup { font-size: 24px; vertical-align: 18px; }
  .included {
    position: absolute; left: 46px; top: 572px; width: 394px; height: 416px;
    background: var(--box); border-radius: 18px;
  }
  .included-heading {
    position: absolute; left: 20px; top: 12px; width: 352px; height: 74px;
  }
  .included-heading text { font-family: "Mr Dafoe", cursive; fill: var(--gold); }
  .perk { position: absolute; display: flex; align-items: center; gap: 9px; white-space: nowrap; }
  .perk-count {
    font-weight: 800; font-size: 48px; color: var(--gold); line-height: 1; width: 30px;
  }
  .perk-label { font-weight: 700; font-size: 16px; line-height: 1.2; }
  .perk-note { position: absolute; font-weight: 700; font-size: 16px; line-height: 1.2; white-space: nowrap; }
  .price-tag {
    position: absolute; left: 0; top: 380px; width: 100%; text-align: center;
    font-weight: 700; font-size: 16px;
  }
  .price-box {
    position: absolute; left: 461px; top: 573px; width: 260px; height: 161px;
    background: var(--box); border-radius: 16px; text-align: center;
  }
  .price-intro { margin-top: 20px; font-weight: 700; font-size: 29px; letter-spacing: 0.5px; }
  .price-amount {
    font-weight: 800; font-size: 86px; line-height: 1; margin-top: 2px; letter-spacing: -2px;
    background: linear-gradient(90deg, #a81ccc, #e23cf4);
    -webkit-background-clip: text; background-clip: text; color: transparent;
  }
  .saving {
    position: absolute; left: 451px; top: 755px; width: 280px; text-align: center;
    font-weight: 700; font-size: 21px; line-height: 1.25;
  }
  .saving em { font-style: normal; color: var(--gold); }
  .seller {
    position: absolute; left: 461px; width: 260px;
    display: flex; justify-content: center; align-items: center; gap: 8px;
    font-weight: 800; font-size: 28px;
  }
  .seller-mark { width: 14px; height: 14px; background: var(--orange); }
  .seller--one { top: 838px; }
  .seller--two { top: 908px; }
  .tickets {
    position: absolute; left: 0; top: 1025px; width: 770px; text-align: center;
    font-weight: 300; font-size: 24px; white-space: nowrap;
  }
  .tickets strong { font-weight: 700; }
</style>
</head>
<body>
<main class="flyer">
  <div class="stage-photo" role="img" aria-label="Nightclub stage with laser lights and two DJs in white t-shirts posing at the decks"></div>

  <svg class="title" viewBox="0 0 770 170" aria-label="The Crimson Ibiza Escape">
    <defs>
      <linearGradient id="titleCyan" x1="0" y1="0" x2="0" y2="1">
        <stop offset="0" stop-color="#ffffff"/>
        <stop offset="1" stop-color="#10e4ff"/>
      </linearGradient>
      <linearGradient id="titleSunset" x1="0" y1="0" x2="1" y2="0">
        <stop offset="0" stop-color="#ffd400"/>
        <stop offset="0.35" stop-color="#ffb400"/>
        <stop offset="0.55" stop-color="#ff6a3a"/>
        <stop offset="0.8" stop-color="#ff1cb4"/>
        <stop offset="1" stop-color="#ff1cb4"/>
      </linearGradient>
    </defs>
    <text class="title-main" x="98" y="73" font-size="84" fill="url(#titleCyan)"
          textLength="574" lengthAdjust="spacingAndGlyphs">THE CRIMSON IBIZA</text>
    <text class="title-accent" x="98" y="157" font-size="78" fill="url(#titleSunset)"
          textLength="574" lengthAdjust="spacingAndGlyphs">ESCAPE</text>
  </svg>

  <p class="dates">Friday 14<sup>th</sup> July - Monday 17<sup>th</sup> July</p>

  <section class="included">
    <svg class="included-heading" viewBox="0 0 352 74" role="heading" aria-level="2" aria-label="Whats included?">
      <text x="2" y="58" font-size="62" textLength="346" lengthAdjust="spacingAndGlyphs">Whats included?</text>
    </svg>
    <div class="perk" style="left:34px;top:114px"><span class="perk-count">4</span><span class="perk-label">Nights Of<br>Entertainment</span></div>
    <div class="perk" style="left:34px;top:179px"><span class="perk-count">6</span><span class="perk-label">Parties in<br>Total</span></div>
    <div class="perk" style="left:34px;top:242px"><span class="perk-count">1</span><span class="perk-label">Boat<br>Party</span></div>
    <div class="perk" style="left:230px;top:112px"><span class="perk-count">1</span><span class="perk-label">Pool<br>Party</span></div>
    <div class="perk" style="left:230px;top:179px"><span class="perk-count">2</span><span class="perk-label">Superclub<br>Parties</span></div>
    <div class="perk" style="left:230px;top:242px"><span class="perk-count">2</span><span class="perk-label">Indoor<br>Water Party</span></div>
    <p class="perk-note" style="left:34px;top:316px">Bottomless Drinks<br>(Boat Party Only)</p>
    <p class="perk-note" style="left:230px;top:316px">An unbelievable<br>experience</p>
    <p class="price-tag">1 unbeatable price.</p>
  </section>

  <section class="price-box">
    <p class="price-intro">ALL THIS FOR</p>
    <p class="price-amount">140€</p>
  </section>

  <p class="saving">YOU SAVE <em>50€</em> WHEN<br>YOU BOOK WITH US</p>

  <p class="seller seller--one"><span class="seller-mark"></span>Ticketlane</p>
  <p class="seller seller--two">Gribolo</p>

  <p class="tickets">Tickets avaialble from <strong>Ticketlane</strong> &amp; <strong>Gribolo</strong></p>
</main>
</body>
</html>
```